Geschäftspapiere für industriellen 3D-Druck
Zielgruppe
Industrieller 3D Druck
Aufgabenstellung
Industrielles, zukunftorientieres Design, ähnliche Farben wie das Logo
In der unteren Briefkopfzeile sollen die Adresse, sowie die Bankdaten aufgeführt werden. In der oberen Briefkopfzeile ebenfalls die Adresse des Unternehmens, sowie das Unternehmenslogo.

```html
<!DOCTYPE html>
<html lang="de">
<head>
<meta charset="utf-8">
<title>Stratavo3D Briefpapier</title>
<link rel="stylesheet" href="https://fonts.googleapis.com/css2?family=Carlito:wght@400;700&display=swap">
<style>
  :root {
    --brand-blue: #0568ae;
    --text-grey: #4a4a4a;
    --wash-light: #e9eff6;
    --wash-mid: #e3f1fa;
    --paper: #ffffff;
  }
  html, body {
    margin: 0;
    padding: 0;
    overflow: hidden;
  }
  .letterhead {
    position: relative;
    width: 846px;
    height: 1200px;
    background: var(--paper);
    font-family: "Carlito", sans-serif;
    color: var(--text-grey);
    overflow: hidden;
  }
  .brand {
    position: absolute;
    top: 98px;
    right: 28px;
    height: 52px;
    display: flex;
    align-items: center;
    gap: 12px;
  }
  .brand-square {
    width: 44px;
    height: 44px;
    background: var(--brand-blue);
  }
  .brand-name {
    font-size: 30px;
    font-weight: 700;
    letter-spacing: 1.5px;
    color: var(--text-grey);
  }
  .brand-bar {
    position: absolute;
    top: 85px;
    left: 827px;
    width: 17px;
    height: 72px;
    background: var(--brand-blue);
  }
  .sender-line {
    position: absolute;
    top: 206px;
    left: 86px;
    margin: 0;
    font-size: 16px;
    line-height: 20px;
    white-space: nowrap;
  }
  .watermark-area {
    position: absolute;
    left: 216px;
    top: 408px;
    width: 415px;
    height: 386px;
    background: linear-gradient(90deg, var(--wash-light), var(--wash-mid), var(--wash-light));
    opacity: 0.8;
  }
  .footer {
    position: absolute;
    top: 0;
    left: 0;
    width: 846px;
    height: 1200px;
    font-size: 14.5px;
    line-height: 14.5px;
  }
  .footer p { margin: 0; white-space: nowrap; }
  .company-block {
    position: absolute;
    left: 68px;
    top: 1104px;
  }
  .divider {
    position: absolute;
    top: 1103px;
    width: 4px;
    height: 58px;
    background: var(--brand-blue);
  }
  .divider-one { left: 302px; }
  .divider-two { left: 487px; }
  .contact-block {
    position: absolute;
    left: 318px;
    top: 1104px;
    list-style: none;
    margin: 0;
    padding: 0;
  }
  .contact-block li {
    display: flex;
    align-items: center;
    gap: 9px;
    height: 14.5px;
    white-space: nowrap;
  }
  .contact-block svg {
    width: 12px;
    height: 12px;
    flex: none;
    fill: none;
    stroke: var(--brand-blue);
    stroke-width: 1.2;
  }
  .bank-block {
    position: absolute;
    left: 516px;
    top: 1103px;
    display: grid;
    grid-template-columns: 116px auto;
    white-space: nowrap;
  }
  .bottom-band {
    position: absolute;
    left: 0;
    top: 1191px;
    width: 846px;
    height: 9px;
    background: var(--brand-blue);
  }
</style>
</head>
<body>
<div class="letterhead">
  <div class="brand">
    <div class="brand-square"></div>
    <span class="brand-name">STRATAVO3D</span>
  </div>
  <div class="brand-bar"></div>

  <p class="sender-line">Alpenrand Medizintechnik AG | your street here 1 | 00000 your city</p>

  <div class="watermark-area" role="img" aria-label="Faint brand watermark area"></div>

  <footer class="footer">
    <div class="company-block">
      <p>Stratavo3D GmbH</p>
      <p>your street here 1</p>
      <p>00000 your city</p>
      <p>Geschaftsfuhrer : Max Mustermann</p>
    </div>
    <div class="divider divider-one"></div>
    <ul class="contact-block">
      <li><svg viewBox="0 0 12 12"><path d="M2 1.5 L4 1.5 L5 4 L3.8 5 Q5 7.5 7 8.2 L8 7 L10.5 8 L10.5 10 Q5 10.5 2 4 Z" fill="#0568ae" stroke="none"/></svg>0000-00 00 00</li>
      <li><svg viewBox="0 0 12 12"><rect x="3" y="1" width="6" height="3"/><rect x="1" y="4" width="10" height="5" rx="1"/><rect x="3" y="7" width="6" height="4"/></svg>0000-00 00 00</li>
      <li><svg viewBox="0 0 12 12"><rect x="1" y="2.5" width="10" height="7" fill="#0568ae" stroke="none"/><path d="M1 2.5 L6 7 L11 2.5" stroke="#fff"/></svg>info@stratavo3d.ch</li>
      <li><svg viewBox="0 0 12 12"><circle cx="6" cy="6" r="5"/><ellipse cx="6" cy="6" rx="2.2" ry="5"/><path d="M1 6 H11 M2 3.5 H10 M2 8.5 H10"/></svg>www.stratavo3d.ch</li>
    </ul>
    <div class="divider divider-two"></div>
    <div class="bank-block">
      <span>Bankverbindung</span><span>Bank Name</span>
      <span>IBAN</span><span>De00 0000 0000 0000 0000</span>
      <span>BIC</span><span>XXXXXXXXXXXXX</span>
      <span>Steuernummer</span><span>000 000 00000</span>
    </div>
  </footer>

  <div class="bottom-band"></div>
</div>
</body>
</html>
```